Electrical contractor in San Diego county since 1988

Provide a company name/ logo for business cards and forms. Newer and more modern old card is attached. Color preference is black and orange. Simple and streamlined nothing too busy. I have also attached a card that represents the simplicity of what we are looking for.

Contractor

```html
<!DOCTYPE html>
<html lang="en">
<head>
<meta charset="utf-8">
<title>Ashford Electric Inc – Business Card</title>
<link rel="stylesheet" href="https://fonts.googleapis.com/css2?family=Open+Sans:wght@400;600;700&display=swap">
<style>
  :root {
    --page-bg: #e9e6e1;
    --card-white: #fbfbfb;
    --card-dark-top: #3a3a3a;
    --card-dark-bottom: #151515;
    --brand-orange: #f26a2e;
    --ink: #2b2b2b;
    --ink-soft: #5a5a5a;
    --on-dark: #f2f2f2;
    --on-dark-soft: #c9c9c9;
  }
  * { box-sizing: border-box; margin: 0; padding: 0; }
  html, body {
    width: 1200px; height: 1023px; overflow: hidden;
    background: var(--page-bg);
    font-family: "Open Sans", Arial, sans-serif;
  }
  .stage {
    width: 1200px; height: 1023px;
    display: flex; align-items: center; justify-content: center; gap: 40px;
  }
  .card {
    width: 540px; height: 309px; position: relative;
    border-radius: 4px; overflow: hidden;
    box-shadow: 0 10px 28px rgba(0,0,0,.18);
  }
  .card--front { background: var(--card-white); color: var(--ink); }
  .card--back {
    background: linear-gradient(160deg, var(--card-dark-top), var(--card-dark-bottom));
    color: var(--on-dark);
    display: flex; flex-direction: column; justify-content: center; padding-left: 70px;
  }
  .brand {
    position: absolute; top: 34px; right: 36px; text-align: right;
  }
  .brand__mark {
    display: inline-block; width: 34px; height: 34px; background: var(--ink); margin-bottom: 10px;
  }
  .brand__name {
    color: var(--brand-orange); font-weight: 600; font-size: 21px; letter-spacing: .5px; text-transform: uppercase;
  }
  .brand__tagline { color: var(--ink-soft); font-size: 12.5px; margin-top: 2px; }
  .details {
    position: absolute; right: 36px; top: 150px; text-align: right;
    font-size: 11.5px; line-height: 1.6; color: var(--ink);
  }
  .details__gap { height: 10px; }
  .details__row { display: flex; justify-content: flex-end; align-items: center; gap: 8px; }
  .details__icon {
    width: 11px; height: 11px; border-radius: 50%; background: var(--brand-orange); flex: none;
  }
  .person { position: absolute; left: 36px; bottom: 38px; }
  .person__name {
    color: var(--brand-orange); font-weight: 700; font-size: 20px; text-transform: uppercase; letter-spacing: .3px;
  }
  .person__title { color: var(--ink); font-size: 13px; margin-top: 2px; }
  .back__name {
    font-weight: 700; font-size: 34px; text-transform: uppercase; letter-spacing: 1px;
  }
  .back__tagline {
    color: var(--on-dark-soft); font-size: 15px; text-transform: uppercase; letter-spacing: 5px; margin-top: 4px;
  }
</style>
</head>
<body>
<main class="stage">
  <section class="card card--front" aria-label="Card front">
    <header class="brand">
      <span class="brand__mark" aria-hidden="true"></span>
      <div class="brand__name">Ashford Electric Inc</div>
      <div class="brand__tagline">Commercial - New &amp; Remodel</div>
    </header>
    <address class="details" style="font-style: normal;">
      <div>P.O. Box 2718 Cedar Flats, CA 92071-0415</div>
      <div>Lic. 402718</div>
      <div class="details__gap"></div>
      <div class="details__row">(555) 014-2286 <span class="details__icon"></span></div>
      <div class="details__row">(555) 014-3390 <span class="details__icon"></span></div>
      <div class="details__row">dana.whitcomb@example.com <span class="details__icon"></span></div>
    </address>
    <div class="person">
      <div class="person__name">Dana Whitcomb</div>
      <div class="person__title">President</div>
    </div>
  </section>

  <section class="card card--back" aria-label="Card back">
    <div class="back__name">Ashford Electric Inc</div>
    <div class="back__tagline">Commercial - New &amp; Remodel</div>
  </section>
</main>
</body>
</html>
```